Construction Company Website Design

I need a Website Design for a Construction Company. I have attached logo and business card design files (a.i) to match styles and text for the website. I will need design for 3 pages:
1. A Home page
2. A secondary page (will be different information pages)
3. A contact page with submision form
Website to look professional and match the 'theme' across all pages, using main colours / reverse colours as per design files. Must be clear it is a construction related website without being over the top. Happy for the construction related details (whether that be images/outlines/backgrounds etc to be fairly subtle and not overbearing on the contect of the pages. It will be the content that will be most important, not the images within.

Content has not yet been fully completed but attached is a site map. Each page will need a space for the insertion of the relevant heading and associated content for that particular page. Example can be used as per attached map. If it is preferable to have content completed for this to be a more succesful project please advise and I will complete and submit.

Target Market(s)

Clients for potential construction projects. These could be a range of people. All would be very professional, well educated and put a substantial expection on the quality of website provided.

Industry/Entity Type

Construction

Number of Pages Required

3 page

Font styles to use
Serif
Sans Serif
Other font styles liked:
• fonts preferable as per design files provided unless designer beleives a different font would suit better

Requirements
Must have
• Colour scheme to match logo and business card files provided. Fonts that match as per provided files. Pages must be consistent with the theme carrying across all pages. All pages must have contact details at the bottom of the page.
• Contents of page 1 - 'Home page': multiple tab options / logo link
• Contents of page 2 - 'Secondary page': Top and side navigation / area for information and/or images.
• Contents of page - 'Contact us page': Top and side navigation / Submission form / area for logos such as linkdin, facebook etc.
Nice to have
• Would be good to have a or some generic construction related images - outlines / shadows / effects etc. These might be background images or outlines related to the relevant industry and are consistent across the pages. Could be outlines of buildings, images of men with hardhats etc etc. Good to see colour scheme as per design files used
Should not have
• No pictures of houses. Generally no photos. If any imagery of people must not show faces/details.

```html
<!DOCTYPE html>
<html lang="en">
<head>
<meta charset="utf-8">
<title>K.R.M Constructions — Home</title>
<link href="https://fonts.googleapis.com/css2?family=Open+Sans:wght@400;600;700;800&display=swap" rel="stylesheet">
<style>
:root{
  --blue:#1a8ad6;
  --blue-dark:#1577bb;
  --ink:#2f2f2f;
  --muted:#7a7a7a;
  --light:#f2f2f2;
  --lighter:#f7f7f7;
  --footer:#3c3c3c;
  --footer-text:#d6d6d6;
  --white:#fff;
}
*{box-sizing:border-box;margin:0;padding:0}
html,body{width:1200px;height:3191px;overflow:hidden}
body{font-family:"Open Sans",Arial,sans-serif;color:var(--ink);background:var(--white);position:relative}
a{color:inherit;text-decoration:none}
section,header,footer{position:relative;width:1200px}

/* Header */
.site-header{height:92px;background:var(--white)}
.brand{position:absolute;left:100px;top:34px;font-size:22px;font-weight:600;letter-spacing:2px;color:#333}
.main-nav{position:absolute;right:100px;top:38px;display:flex;gap:42px;font-size:13px;color:#444}
.main-nav a.active{color:var(--blue);padding-bottom:8px;border-bottom:2px solid var(--blue)}

/* Hero */
.hero{height:617px;overflow:hidden}
.hero-photo{position:absolute;inset:0;background:linear-gradient(180deg,#9a9a9a 0%,#6e6e6e 45%,#3f3f3f 100%)}
.hero-title{position:absolute;top:270px;width:100%;text-align:center;color:var(--white);font-size:84px;font-weight:800;letter-spacing:1px}
.hero-sub{position:absolute;top:378px;width:100%;text-align:center;color:var(--white);font-size:19px}
.hero-arrow{position:absolute;top:309px;width:44px;height:44px;border-radius:50%;background:rgba(255,255,255,.18)}
.hero-arrow.prev{left:27px}.hero-arrow.next{right:29px}
.hero-arrow svg{position:absolute;left:13px;top:12px}

/* About */
.about{height:447px;background:var(--blue);color:var(--white);text-align:center}
.section-title{font-size:37px;font-weight:700;text-transform:uppercase;padding-top:70px;line-height:1.2}
.section-title::after{content:"";display:block;width:80px;height:3px;background:var(--blue);margin:8px auto 0}
.about .section-title::after{background:var(--white)}
.about p{width:1020px;margin:0 auto;font-size:13px;line-height:23px}
.about p:first-of-type{margin-top:22px}
.about p+p{margin-top:16px}
.btn-outline{display:inline-block;margin-top:50px;width:160px;height:44px;line-height:40px;border:2px solid var(--white);font-size:14px;font-weight:600}
.btn{display:inline-block;height:42px;line-height:42px;padding:0 34px;background:var(--blue);color:var(--white);font-size:14px;font-weight:600}

/* Services */
.services{height:657px;background:var(--light);text-align:center}
.services .section-title,.blog .section-title,.partners .section-title{color:#333}
.service-list{display:flex;justify-content:center;gap:0;margin-top:60px}
.service{width:275px}
.service-icon{width:112px;height:112px;margin:0 auto;border-radius:50%;border:1px solid #e1e1e1;background:var(--white);display:flex;align-items:center;justify-content:center}
.service-icon.is-active{background:var(--blue);border-color:var(--blue)}
.service h3{font-size:19px;font-weight:600;margin-top:20px}
.service.is-active h3{color:var(--blue)}
.service p{font-size:13px;line-height:21px;color:var(--muted);width:200px;margin:10px auto 0}
.services .btn{margin-top:86px}

/* Blog */
.blog{height:602px;background:var(--lighter);text-align:center}
.blog-grid{display:flex;gap:43px;justify-content:center;margin-top:66px}
.post{position:relative;width:304px;height:236px;border:4px solid var(--white);box-shadow:0 0 0 1px #e2e2e2;text-align:left;overflow:hidden}
.post-photo{position:absolute;inset:0}
.post:nth-child(1) .post-photo{background:linear-gradient(160deg,#8a7f72,#3a4a6a)}
.post:nth-child(2) .post-photo{background:linear-gradient(160deg,#5a5a5a,#3e3e3e)}
.post:nth-child(3) .post-photo{background:linear-gradient(160deg,#8a6a4c,#4b3b2e)}
.post-body{position:absolute;left:12px;right:12px;bottom:22px;color:var(--white)}
.post h3{font-size:17px;font-weight:800;line-height:21px;text-transform:uppercase}
.post time{display:block;font-size:12px;margin-top:8px}
.post .read-more{display:block;font-size:13px;font-weight:700;color:var(--blue);margin-top:16px;text-transform:uppercase}
.post.is-hover .post-body{bottom:auto;top:68px}
.blog .btn{margin-top:70px;padding:0 30px;height:40px;line-height:40px;font-size:13px}

/* Partners */
.partners{height:400px;background:var(--white);text-align:center}
.partner-row{display:flex;gap:17px;justify-content:center;margin-top:70px}
.partner{width:180px;height:122px;border:2px solid #dedede;display:flex;align-items:center;justify-content:center;font-size:18px;font-weight:700;color:#333;letter-spacing:1px;text-transform:uppercase}
.partner-arrow{position:absolute;top:2648px}
.partner-arrow{top:236px}
.partner-arrow.prev{left:80px}.partner-arrow.next{right:80px}

/* Footer */
.site-footer{height:376px;background:var(--footer);color:var(--footer-text);font-size:13px}
.footer-brand{position:absolute;left:100px;top:98px;font-size:19px;font-weight:600;letter-spacing:2px;color:var(--white)}
.footer-about{position:absolute;left:100px;top:143px;width:250px;line-height:20px;font-size:12px}
.footer-more{position:absolute;left:100px;top:225px;color:var(--blue);font-size:12px}
.footer-heading{position:absolute;top:66px;color:var(--blue);font-size:14px;font-weight:600;text-transform:uppercase}
.footer-heading::after{content:"";display:block;width:135px;height:1px;background:#8a8a8a;margin-top:10px}
.links{position:absolute;top:127px;list-style:none;line-height:28px}
.contact{position:absolute;left:862px;top:127px;list-style:none;line-height:28px}
.contact li{display:flex;align-items:center;gap:9px}
.contact li.indent{padding-left:21px}
.footer-bottom{position:absolute;left:100px;right:100px;top:308px;border-top:1px solid #555;text-align:center;padding-top:22px;font-size:12px}
</style>
</head>
<body>

<header class="site-header">
  <a class="brand" href="#">K.R.M CONSTRUCTIONS</a>
  <nav class="main-nav">
    <a class="active" href="#">HOME</a>
    <a href="#">ABOUT US</a>
    <a href="#">SERVICES</a>
    <a href="#">PROJECTS</a>
    <a href="#">CULTURE</a>
    <a href="#">NEWS</a>
    <a href="#">CONTACT</a>
  </nav>
</header>

<section class="hero">
  <div class="hero-photo" role="img" aria-label="Black and white photo of rolled building plans and a hard hat on a desk with cranes in the background"></div>
  <h1 class="hero-title">K.R.M CONSTRUCTIONS</h1>
  <p class="hero-sub">Cumque nihil impedit quo minus id quod maxime placeat facere possimus omnis assumenda</p>
  <span class="hero-arrow prev"><svg width="18" height="20" viewBox="0 0 18 20"><path d="M12 2 4 10l8 8" fill="none" stroke="#fff" stroke-width="2"/></svg></span>
  <span class="hero-arrow next"><svg width="18" height="20" viewBox="0 0 18 20"><path d="M6 2l8 8-8 8" fill="none" stroke="#fff" stroke-width="2"/></svg></span>
</section>

<section class="about">
  <h2 class="section-title">About K.R.M Constructions</h2>
  <p>Sed ut perspiciatis unde omnis iste natus error sit voluptatem accusantium doloremque laudantium, totam rem aperiam, eaque ipsa quae ab illo inventore veritatis et quasi architecto beatae vitae dicta sunt explicabo. Nemo enim ipsam voluptatem quia voluptas sit aspernatur aut odit aut fugit, sed quia consequuntur magni dolores eos qui ratione voluptatem sequi nesciunt</p>
  <p>But I must explain to you how all this mistaken idea of denouncing pleasure and praising pain was born and I will give you a complete account of the system, and expound the actual teachings of the great explorer of the truth, the master-builder of human happiness.</p>
  <a class="btn-outline" href="#">LEARN MORE</a>
</section>

<section class="services">
  <h2 class="section-title">Our Services</h2>
  <div class="service-list">
    <div class="service">
      <div class="service-icon"><svg width="46" height="46" viewBox="0 0 46 46" fill="none" stroke="#1a8ad6" stroke-width="2"><rect x="10" y="8" width="26" height="34"/><path d="M4 42h38M16 14h4M26 14h4M16 21h4M26 21h4M16 28h4M26 28h4M20 42v-7h6v7"/></svg></div>
      <h3>Commercial</h3>
      <p>Temporibus autem quibusdam et aut officiis debitis aut rerum necessitatibus saepe eveniet ut et voluptates repudiandae .</p>
    </div>
    <div class="service">
      <div class="service-icon"><svg width="46" height="46" viewBox="0 0 46 46" fill="none" stroke="#1a8ad6" stroke-width="2"><path d="M5 22 23 8l18 14M10 18v22h26V18M19 40v-10h8v10M4 40h38"/></svg></div>
      <h3>Residential</h3>
      <p>Temporibus autem quibusdam et aut officiis debitis aut rerum necessitatibus saepe eveniet ut et voluptates repudiandae .</p>
    </div>
    <div class="service is-active">
      <div class="service-icon is-active"><svg width="46" height="46" viewBox="0 0 46 46" fill="none" stroke="#fff" stroke-width="2.4"><path d="M30 6a9 9 0 0 0-9 12L7 32a4 4 0 0 0 6 6l14-14A9 9 0 0 0 39 14l-6 5-5-1-1-5 5-6z"/></svg></div>
      <h3>Building Maintenance</h3>
      <p>Temporibus autem quibusdam et aut officiis debitis aut rerum necessitatibus saepe eveniet ut et voluptates repudiandae .</p>
    </div>
    <div class="service">
      <div class="service-icon"><svg width="46" height="46" viewBox="0 0 46 46" fill="none" stroke="#1a8ad6" stroke-width="2"><rect x="10" y="8" width="26" height="34" rx="2"/><path d="M17 5h12v6H17zM16 20l3 3 6-6M16 32l3 3 6-6M28 22h4M28 34h4"/></svg></div>
      <h3>Project Management</h3>
      <p>Temporibus autem quibusdam et aut officiis debitis aut rerum necessitatibus saepe eveniet ut et voluptates repudiandae .</p>
    </div>
  </div>
  <a class="btn" href="#">VIEW MORE</a>
</section>

<section class="blog">
  <h2 class="section-title">Our Blog</h2>
  <div class="blog-grid">
    <article class="post">
      <div class="post-photo" role="img" aria-label="Photo of workers in blue overalls on a building site, shown from behind"></div>
      <div class="post-body"><h3>Nostrum exercitationem ullam corporis</h3><time>APRIL 14, 2015</time></div>
    </article>
    <article class="post is-hover">
      <div class="post-photo" role="img" aria-label="Darkened photo of a concrete building structure"></div>
      <div class="post-body"><h3>Eiusmod tempor incididunt ut labore</h3><time>JANUARY 20, 2015</time><a class="read-more" href="#">Read more</a></div>
    </article>
    <article class="post">
      <div class="post-photo" role="img" aria-label="Overhead photo of builders working on scaffolding"></div>
      <div class="post-body"><h3>Numquam eius modi tempora incidunt</h3><time>APRIL 14, 2015</time></div>
    </article>
  </div>
  <a class="btn" href="#">VIEW ALL BLOG</a>
</section>

<section class="partners">
  <h2 class="section-title">Client Partner</h2>
  <div class="partner-row">
    <div class="partner">Ironvale</div>
    <div class="partner">Northline</div>
    <div class="partner">Stonebridge</div>
    <div class="partner">Calder</div>
    <div class="partner">Ridgeway</div>
  </div>
  <svg class="partner-arrow prev" width="20" height="44" viewBox="0 0 20 44"><path d="M18 2 2 22l16 20" fill="none" stroke="#d4d4d4" stroke-width="2"/></svg>
  <svg class="partner-arrow next" width="20" height="44" viewBox="0 0 20 44"><path d="M2 2l16 20L2 42" fill="none" stroke="#d4d4d4" stroke-width="2"/></svg>
</section>

<footer class="site-footer">
  <div class="footer-brand">K.R.M CONSTRUCTIONS</div>
  <p class="footer-about">But I must explain to you how all this mistaken idea of denouncing pleasure and praising pain was born and I will give you a complete...</p>
  <a class="footer-more" href="#">read more...</a>

  <h4 class="footer-heading" style="left:449px">Quick Links</h4>
  <ul class="links" style="left:449px">
    <li><a href="#">Home</a></li><li><a href="#">About Us</a></li><li><a href="#">Services</a></li><li><a href="#">Culture</a></li><li><a href="#">News</a></li>
  </ul>
  <ul class="links" style="left:636px">
    <li><a href="#">Terms &amp; Conditions</a></li><li><a href="#">Privacy Policy</a></li><li><a href="#">Contact</a></li>
  </ul>

  <h4 class="footer-heading" style="left:862px">Contact Us</h4>
  <ul class="contact">
    <li><svg width="12" height="14" viewBox="0 0 12 14"><path d="M6 0a5 5 0 0 0-5 5c0 4 5 9 5 9s5-5 5-9a5 5 0 0 0-5-5z" fill="#1a8ad6"/><circle cx="6" cy="5" r="2" fill="#3c3c3c"/></svg>K.R.M Constructions Pty Limited</li>
    <li class="indent">14 Harbour Lane Westfield 2190</li>
    <li><svg width="12" height="12" viewBox="0 0 12 12"><path d="M2 0h3l1 3-2 1a7 7 0 0 0 4 4l1-2 3 1v3a2 2 0 0 1-2 2A10 10 0 0 1 0 2a2 2 0 0 1 2-2z" fill="#1a8ad6"/></svg>0400 123 456</li>
    <li><svg width="12" height="10" viewBox="0 0 12 10"><rect width="12" height="10" fill="#1a8ad6"/><path d="M0 0l6 5 6-5" fill="none" stroke="#3c3c3c"/></svg>info@krmbuild.com.au</li>
    <li><svg width="12" height="12" viewBox="0 0 12 12"><rect width="12" height="12" fill="#1a8ad6"/></svg>www.krmbuild.com.au</li>
  </ul>

  <div class="footer-bottom">© 2018 K.R.M CONSTRUCTIONS . All right reserved . Term of Use</div>
</footer>

</body>
</html>
```